Looking to design a new sign for our church.

Looking for a new sign
4 x 8 feet dimension
We are renaming the church "Medlow Ridge Community Church"
looking for legible graphics
Would like some type of backdrop being a family tree (oak) / open to other ideas as you are led
I have included a pic of the old sign for your review
would like to incorporate our ministry logo on the lower right hand corner of the sign / see file attached

```html
<!DOCTYPE html>
<html lang="en">
<head>
<meta charset="utf-8">
<title>Medlow Ridge Community Church – Sign</title>
<link rel="stylesheet" href="https://fonts.googleapis.com/css2?family=Fira+Sans+Extra+Condensed:wght@600&display=swap">
<style>
  :root {
    --page: #ffffff;
    --sign-bg: #08433a;
    --leaf-light: #6cb33f;
    --leaf-mid: #4c9e38;
    --leaf-deep: #2f7d2e;
    --title-top: #3f9a3a;
    --title-bottom: #74b93f;
    --mark: #5aa83a;
  }
  html, body {
    margin: 0;
    padding: 0;
    width: 927px;
    height: 1200px;
    overflow: hidden;
    background: var(--page);
  }
  .canvas {
    position: relative;
    width: 927px;
    height: 1200px;
  }
  .sign {
    position: absolute;
    left: 25px;
    top: 382px;
    width: 877px;
    height: 436px;
    background: var(--sign-bg);
    overflow: hidden;
  }
  .sign__tree {
    position: absolute;
    left: 0;
    top: 0;
    width: 877px;
    height: 436px;
  }
  .sign__title {
    position: absolute;
    left: 60px;
    width: 640px;
    top: 247px;
    margin: 0;
    text-align: center;
    font-family: "Fira Sans Extra Condensed", "Arial Narrow", sans-serif;
    font-weight: 600;
    font-size: 70px;
    line-height: 70px;
    letter-spacing: 2px;
    text-transform: uppercase;
    background: linear-gradient(180deg, var(--title-top) 0%, var(--title-bottom) 100%);
    -webkit-background-clip: text;
    background-clip: text;
    color: transparent;
  }
  .sign__title span { display: block; }
  .ministry-mark {
    position: absolute;
    left: 712px;
    top: 240px;
    width: 130px;
    display: flex;
    flex-direction: column;
    align-items: center;
    gap: 10px;
  }
  .ministry-mark__dot {
    width: 110px;
    height: 110px;
    border-radius: 50%;
    background: var(--mark);
  }
  .ministry-mark__name {
    font-family: "Fira Sans Extra Condensed", "Arial Narrow", sans-serif;
    font-weight: 600;
    font-size: 24px;
    line-height: 1;
    color: var(--mark);
    text-transform: uppercase;
    white-space: nowrap;
  }
</style>
</head>
<body>
<main class="canvas">
  <section class="sign" aria-label="Medlow Ridge Community Church sign">
    <svg class="sign__tree" viewBox="0 0 877 436" role="img" aria-label="Illustrated leafy oak branches sweeping across the top of the sign, with the trunk curving down the left edge">
      <defs>
        <linearGradient id="foliage" x1="0" y1="0" x2="1" y2="0.4">
          <stop offset="0" stop-color="var(--leaf-deep)"/>
          <stop offset="0.5" stop-color="var(--leaf-mid)"/>
          <stop offset="1" stop-color="var(--leaf-light)"/>
        </linearGradient>
      </defs>
      <path fill="url(#foliage)" d="M0 0 H450 C520 40 600 90 640 140 C650 175 610 205 555 210 C460 218 360 200 270 205 C170 212 95 240 70 300 C50 350 60 400 160 420 C220 430 260 434 280 436 H0 Z"/>
    </svg>

    <h1 class="sign__title">
      <span>Medlow Ridge</span>
      <span>Community Church</span>
    </h1>

    <div class="ministry-mark">
      <div class="ministry-mark__dot"></div>
      <div class="ministry-mark__name">Harvest Reach</div>
    </div>
  </section>
</main>
</body>
</html>
```